E-learning Information & Community Website Needs a Makeover

I'm looking for a design makeover for my website "Vetrola.club". Vetrola's aim is to connect people to online learning through forums, information, guides & independent reviews. The site was launched in September 2014 using a forum software (Xenforo), but now needs a more polished and sophisticated look which communicates expertise and professionalism. I would like to see designs that use the current "Vetrola" blue (#0070c0). To visit the current website, go to http://www.vetrola.club/

Target Market(s)

People wishing to study online

Industry/Entity Type

Club

Number of Pages Required

4 page

Font styles to use
Sans Serif

Requirements
Must have
• A simple, clear and sophisticated lading page with links to the site's key features: discussion forums, Useful resources, Reviews, News etc, Articles. (See layout idea file attached)
• The main pages are the Landing Page, Discussion Forums, Resources & Reviews
• I would like to see designs that use the current "Vetrola" blue (#0070c0).
Nice to have
• Something uncluttered and easy to understand. The design should convey expertise in the field of online learning, giving users a sense of trust in the site's offerings.
• To give an idea of the sort of thing I'm after, take a look at brantivo.com website (screenshot attached)

```html
<!DOCTYPE html>
<html lang="en">
<head>
<meta charset="utf-8">
<title>Vetrola – Connecting People to Online Learning</title>
<link href="https://fonts.googleapis.com/css2?family=Open+Sans:wght@300;400;600;700&display=swap" rel="stylesheet">
<style>
:root{
  --brand:#0070c0;
  --brand-mid:#0a86d0;
  --sky:#2fc6ec;
  --cyan:#5fd6f4;
  --pale-blue:#c3d8ee;
  --link:#1aa3e0;
  --muted:#8fb8d8;
  --meta:#b9c9d6;
  --green:#8dd33f;
  --yellow:#f4c443;
  --red:#e8605f;
  --orange:#f07d1a;
  --line:#d9e6ef;
  --white:#fff;
  --ink:#4a4a4a;
}
*{margin:0;padding:0;box-sizing:border-box}
html,body{width:1200px;height:1057px;overflow:hidden;background:var(--white)}
body{font-family:"Open Sans",sans-serif;position:relative}
a{text-decoration:none;color:inherit}

.topbar{position:absolute;top:0;left:0;width:1200px;height:40px;font-size:11px;color:var(--muted)}
.topbar .util{position:absolute;left:178px;top:12px}
.topbar .util span{margin:0 6px;color:#c8d6e2}
.topbar .lang{position:absolute;left:632px;top:12px}
.topbar .lang span{margin:0 8px;color:#c8d6e2}
.social{position:absolute;left:767px;top:9px;display:flex;gap:7px}
.social i{display:block;width:22px;height:22px;border-radius:50%;background:var(--sky)}
.topbar .account{position:absolute;left:901px;top:12px}
.topbar .account span{margin:0 8px;color:#c8d6e2}

.mainnav{position:absolute;top:40px;left:0;width:1200px;height:77px;background:var(--brand);color:var(--white)}
.brand{position:absolute;left:177px;top:16px}
.brand .name{font-size:25px;font-weight:300;line-height:30px;letter-spacing:.3px}
.brand .tag{font-size:10.4px;margin-top:4px}
.menu{position:absolute;left:405px;top:32px;display:flex;align-items:center;font-size:11.6px;font-weight:700;letter-spacing:0}
.menu a{margin-right:22px}
.menu svg{margin-right:19px}

.hero{position:absolute;top:117px;left:0;width:1200px;height:533px;background:linear-gradient(180deg,#38cbee,#2cc2ea)}
.hero-photo{position:absolute;inset:0;background:radial-gradient(ellipse at 18% 60%,rgba(20,110,190,.35),transparent 45%),radial-gradient(ellipse at 88% 60%,rgba(20,110,190,.3),transparent 40%),radial-gradient(ellipse at 50% 20%,rgba(20,110,190,.18),transparent 30%)}
.hero h1{position:absolute;top:44px;width:1200px;text-align:center;color:var(--white);font-weight:300;font-size:39px;line-height:36px;letter-spacing:-.4px}
.cta{position:absolute;left:507px;top:151px;width:190px;height:43px;border-radius:22px;background:var(--orange);color:var(--white);font-weight:700;font-size:14px;line-height:43px;text-align:center;letter-spacing:.3px}

.tiles{position:absolute;left:213px;top:231px;width:777px;height:259px;display:grid;grid-template-columns:repeat(6,1fr);grid-template-rows:repeat(2,1fr)}
.tile{position:relative;display:flex;align-items:center;justify-content:center;background:var(--white);color:var(--ink);font-size:15px;text-align:center;line-height:17px}
.tile.icon{color:var(--white)}
.tile.label.left::before{content:"";position:absolute;left:-1px;top:50%;margin-top:-8px;border:8px solid transparent;border-right-color:var(--white);transform:translateX(-15px)}
.tile.label.right::after{content:"";position:absolute;right:-1px;top:50%;margin-top:-8px;border:8px solid transparent;border-left-color:var(--white);transform:translateX(15px);z-index:2}
.green{background:var(--green)}.paleblue{background:var(--pale-blue)}.cyan{background:var(--cyan)}
.yellow{background:var(--yellow)}.blue{background:var(--brand-mid)}.red{background:var(--red)}

.threads{position:absolute;left:191px;top:678px;width:590px}
.threads .head{font-size:12px;color:var(--muted);height:22px;position:relative}
.threads .head .r{position:absolute;left:479px}
.threads .head .v{position:absolute;left:535px}
.thread{position:relative;height:85px}
.avatar{position:absolute;left:14px;top:6px;width:50px;height:50px;border-radius:50%;background:var(--brand);color:var(--white);font-size:11px;line-height:15px;text-align:center;padding-top:14px}
.avatar.photo{background:linear-gradient(160deg,#8a7a6a,#3f3530)}
.badge{position:absolute;left:10px;top:53px;width:58px;height:20px;border-radius:10px;font-size:10px;font-weight:700;color:var(--white);text-align:center;line-height:20px;letter-spacing:.3px}
.badge.advice{background:var(--green)}.badge.news{background:var(--brand-mid)}.badge.article{background:var(--red)}
.thread .title{position:absolute;left:87px;top:21px;font-size:15px;color:var(--link);white-space:nowrap}
.thread .meta{position:absolute;left:88px;top:44px;font-size:10px;color:var(--meta);white-space:nowrap}
.thread .replies{position:absolute;left:485px;top:27px;width:30px;height:25px;background:var(--brand);color:var(--white);font-size:14px;text-align:center;line-height:25px}
.thread .replies::after{content:"";position:absolute;left:18px;bottom:-5px;border:3px solid transparent;border-top:3px solid var(--brand);border-left:3px solid var(--brand)}
.thread .replies.zero{background:var(--pale-blue)}
.thread .replies.zero::after{border-top-color:var(--pale-blue);border-left-color:var(--pale-blue)}
.thread .views{position:absolute;left:543px;top:27px;font-size:15px;color:var(--brand);line-height:25px}
.thread .rule{position:absolute;left:87px;right:4px;bottom:0;height:2px;background:var(--line)}

.poll{position:absolute;left:814px;top:650px;width:220px;height:210px;background:var(--brand);color:var(--white)}
.poll h3{font-weight:400;font-size:15px;line-height:18px;text-align:center;margin-top:26px}
.option{position:absolute;left:29px;width:180px}
.option .lbl{font-size:12px;margin-left:36px}
.option .bar{position:relative;height:15px;margin-top:6px;width:132px;background:#1c80cb;border-radius:8px}
.option .bar i{position:absolute;left:0;top:0;bottom:0;border-radius:8px;background:#29b7ea}
.option .count{position:absolute;left:136px;top:23px;font-size:8px}

.seen{position:absolute;left:814px;top:880px;width:220px}
.seen h3{font-weight:400;font-size:15px;color:var(--brand);text-align:center;margin-bottom:15px}
.seen .item{position:relative;height:73px;padding-left:50px}
.seen .item .pic{position:absolute;left:0;top:4px;width:37px;height:37px;border-radius:50%;background:linear-gradient(160deg,#c9a88a,#6c5444)}
.seen .item .t{font-size:12px;color:var(--link);line-height:14px}
.seen .item .m{font-size:10px;color:var(--meta);margin-top:6px}
.seen .item .rule{position:absolute;left:50px;right:0;bottom:0;height:2px;background:var(--line)}
</style>
</head>
<body>

<header class="topbar">
  <div class="util"><a>Recent Activity</a><span>|</span><a>What's New?</a><span>|</span><a>Help</a></div>
  <div class="lang"><a>English</a><span>|</span><a>Español</a></div>
  <div class="social" aria-label="Social links"><i></i><i></i><i></i><i></i></div>
  <div class="account"><a>Sign up</a><span>|</span><a>Log in</a></div>
</header>

<nav class="mainnav">
  <div class="brand">
    <div class="name">Vetrola</div>
    <div class="tag">Connecting People to Online Learning</div>
  </div>
  <div class="menu">
    <svg width="14" height="14" viewBox="0 0 14 14"><path d="M7 0 0 6.5h2V14h3.5V9.5h3V14H12V6.5h2z" fill="#fff"/></svg>
    <a>FORUMS</a><a>RESOURCES</a><a>MEMBERS</a><a style="margin-right:26px">FAQ</a><a style="margin-right:26px">BLOG</a><a>VETROLA ESPAÑOL</a><a>STUDY SCOOP</a>
  </div>
</nav>

<section class="hero">
  <div class="hero-photo" role="img" aria-label="Photo of joyful people jumping, tinted in bright blue"></div>
  <h1>At the heart of connecting<br>people to online learning</h1>
  <a class="cta">SIGN UP FOR FREE</a>

  <div class="tiles">
    <div class="tile icon green"><svg width="38" height="38" viewBox="0 0 38 38"><path d="M0 0 38 19 0 38z" fill="#fff"/></svg></div>
    <div class="tile label left">Getting<br>started</div>
    <div class="tile icon paleblue"><svg width="50" height="50" viewBox="0 0 50 50"><path d="M0 0h50v19H32l-7 6-7-6H0z M0 28h18l7 6 7-6h18v22H0z" fill="#fff"/></svg></div>
    <div class="tile label left">Discussions</div>
    <div class="tile icon cyan"><svg width="56" height="52" viewBox="0 0 56 52"><g fill="#fff"><path id="s" d="m8 0 2.4 5 5.5.7-4 3.8 1 5.4L8 12.3 3.1 14.9l1-5.4-4-3.8L5.6 5z"/><use href="#s" x="20" y="-2"/><use href="#s" x="40" y="12"/><use href="#s" x="0" y="12"/><use href="#s" x="8" y="34"/><use href="#s" x="32" y="34"/></g></svg></div>
    <div class="tile label left">Reviews</div>

    <div class="tile label right">Tips &amp;<br>Guidelines</div>
    <div class="tile icon yellow"><svg width="44" height="66" viewBox="0 0 44 66"><g fill="#fff"><rect x="19" y="0" width="5" height="66"/><path d="M4 8h32l6 6-6 6H4z"/><path d="M40 24H8l-6 6 6 6h32z"/><path d="M4 40h32l5 5-5 5H4z"/></g></svg></div>
    <div class="tile label right">News &amp;<br>Articles</div>
    <div class="tile icon blue"><svg width="56" height="44" viewBox="0 0 56 44"><g fill="none" stroke="#fff" stroke-width="2.5"><rect x="7" y="1.5" width="47" height="41"/><path d="M7 10H2v30a3 3 0 0 0 5 0"/></g><g fill="#fff"><rect x="13" y="8" width="18" height="13"/><rect x="34" y="8" width="14" height="3"/><rect x="34" y="14" width="14" height="3"/><rect x="34" y="20" width="14" height="3"/><rect x="13" y="26" width="35" height="3"/><rect x="13" y="32" width="35" height="3"/></g></svg></div>
    <div class="tile label right">Newsletter</div>
    <div class="tile icon red"><svg width="46" height="46" viewBox="0 0 46 46"><g fill="none" stroke="#fff" stroke-width="2.5"><path d="M2 18v26h42V18"/><path d="M2 18 23 4l21 14"/><path d="M2 44 18 30M44 44 28 30"/><path d="M2 18l21 16 21-16"/><path d="M9 24V2h22l6 6v16"/></g></svg></div>
  </div>
</section>

<section class="threads">
  <div class="head"><span>Recent Threads</span><span class="r">Replies</span><span class="v">Views</span></div>

  <article class="thread">
    <div class="avatar">Vetrola</div><div class="badge advice">ADVICE</div>
    <a class="title">Best platforms to showcase your digital portfolio</a>
    <div class="meta">By Marisol on Friday at 4:02 PM, MOOC Advice</div>
    <div class="replies">5</div><div class="views">46</div><div class="rule"></div>
  </article>
  <article class="thread">
    <div class="avatar">Vetrola</div><div class="badge news">NEWS</div>
    <a class="title">New open, shareable steps in Stepwise courses</a>
    <div class="meta">By Marisol on Friday at 3:46 PM, Stepwise</div>
    <div class="replies">3</div><div class="views">47</div><div class="rule"></div>
  </article>
  <article class="thread" style="height:89px">
    <div class="avatar photo" style="top:10px" role="img" aria-label="Member profile photo"></div><div class="badge advice" style="top:57px">ADVICE</div>
    <a class="title" style="top:24px">Best platforms to showcase your digital portfolio</a>
    <div class="meta" style="top:48px">By PeterK on Thursday at 9:44 AM, MOOC Advice</div>
    <div class="replies zero" style="top:30px">0</div><div class="views" style="top:30px">31</div><div class="rule"></div>
  </article>
  <article class="thread">
    <div class="avatar photo" role="img" aria-label="Member profile photo"></div><div class="badge article">ARTICLE</div>
    <a class="title">New open, shareable steps in Stepwise courses</a>
    <div class="meta">By Tomas Ferrer on Wednesday at 7:02 PM, Blog</div>
    <div class="replies">1</div><div class="views">108</div><div class="rule"></div>
  </article>
  <article class="thread"><div class="avatar" style="top:8px"></div></article>
</section>

<aside class="poll">
  <h3>What type of course<br>do you prefer?</h3>
  <div class="option" style="top:81px"><div class="lbl">Self-Paced</div><div class="bar"><i style="width:93px"></i></div><div class="count">15 vote(s)</div></div>
  <div class="option" style="top:132px"><div class="lbl">Scheduled</div><div class="bar"><i style="width:59px"></i></div><div class="count">12 vote(s)</div></div>
</aside>

<aside class="seen">
  <h3>Have you seen?</h3>
  <div class="item">
    <div class="pic" role="img" aria-label="Member profile photo"></div>
    <div class="t">Lernix vs Corvana: what's the difference?</div>
    <div class="m">By LKane, Replies: 15</div><div class="rule"></div>
  </div>
  <div class="item" style="padding-top:5px">
    <div class="pic" style="top:7px" role="img" aria-label="Member profile photo"></div>
    <div class="t">Peer assessment on MOOCs - a good thing or a bad thing?</div>
    <div class="m">By PeterK, Replies: 8</div>
  </div>
</aside>

</body>
</html>
```